Billboard design - consider what a billboard is

Design a billboard using my logo - Billboard is 6m x 3m
A Billboard is advertising for my company that is on a big sign.

Has to be clean and easy to read, and ideally highlights that we are Residential and Commercial builders.

Keep it clean and easy to read

The contact number for the board is

022 583 7092
www.harbourframeworks.co.nz
info@harbourframeworks.co.nz

Doesnt have to have all contact details if it doesnt fit

Has to catch peoples attention to contact us if they need a builder

Can you please change the sign to be all white writing, with black background ?
Updates

Please consider what a billboard is...

The design needs to be suitable for a billboard..

Target Market(s)

people driving past

Industry/Entity Type

Construction

Logo Text

Wellington Builder, website email address, contact number

Colors
0054AA
0677BA
7BADD7
CADEEF
E8F1F8

Requirements
Must have
• Easy to read
Nice to have
• easy to read, can clearly see contact details

```html
<!DOCTYPE html>
<html lang="en">
<head>
<meta charset="utf-8">
<title>Harbour Frameworks Billboard</title>
<link href="https://fonts.googleapis.com/css2?family=Poppins:wght@500;600;700&display=swap" rel="stylesheet">
<style>
  :root {
    --page-bg: #e6e9ee;
    --navy: #1f2a5c;
    --white: #ffffff;
    --accent-yellow: #f6c21c;
    --photo-sky: #7fa9d6;
    --photo-mid: #c9d3dc;
    --photo-low: #5b5f63;
    --brand-blue: #0054aa;
  }
  * { margin: 0; padding: 0; box-sizing: border-box; }
  html, body {
    width: 1200px; height: 800px; overflow: hidden;
    background: var(--page-bg);
    font-family: "Poppins", sans-serif;
  }
  .canvas { position: relative; width: 1200px; height: 800px; }
  .billboard-frame {
    position: absolute; left: 30px; top: 114px;
    width: 1140px; height: 571px; overflow: hidden;
    box-shadow: 0 8px 24px rgba(0,0,0,0.18);
  }
  .billboard {
    position: absolute; left: 0; top: 0;
    width: 1507px; height: 755px;
    transform: scale(0.7565); transform-origin: 0 0;
  }
  .billboard-art { position: absolute; inset: 0; }
  .copy { position: absolute; left: 68px; color: var(--white); white-space: nowrap; }
  .headline {
    top: 52px; font-weight: 700; font-size: 74px;
    line-height: 90px; letter-spacing: 2px;
  }
  .tagline {
    top: 326px; font-weight: 500; font-size: 41px; letter-spacing: 1.5px;
  }
  .call-to-action {
    top: 496px; font-weight: 700; font-size: 33px;
    letter-spacing: 1.5px; color: var(--accent-yellow);
  }
  .phone {
    top: 550px; font-weight: 700; font-size: 68px; letter-spacing: 2px;
  }
  .website {
    top: 638px; font-weight: 600; font-size: 37px; letter-spacing: 1px;
  }
  .brand-plate {
    position: absolute; left: 1165px; top: 533px;
    width: 275px; height: 153px; background: var(--white);
    display: flex; align-items: center; justify-content: center; gap: 12px;
  }
  .brand-square { width: 22px; height: 22px; background: var(--brand-blue); flex: none; }
  .brand-name {
    font-weight: 700; font-size: 28px; line-height: 1.05;
    color: var(--brand-blue); text-align: left;
  }
</style>
</head>
<body>
<div class="canvas">
  <div class="billboard-frame">
    <div class="billboard">
      <svg class="billboard-art" viewBox="0 0 1507 755" width="1507" height="755">
        <defs>
          <linearGradient id="photoTone" x1="0" y1="0" x2="0" y2="1">
            <stop offset="0" stop-color="var(--photo-sky)"/>
            <stop offset="0.45" stop-color="var(--photo-mid)"/>
            <stop offset="1" stop-color="var(--photo-low)"/>
          </linearGradient>
        </defs>
        <rect x="760" y="0" width="747" height="755" fill="url(#photoTone)"
              role="img" aria-label="Photo of a multi-storey commercial building under scaffolding with neighbouring towers and blue sky"/>
        <path d="M0 0 H965 C830 120 785 280 785 400 C785 540 860 680 965 755 H0 Z" fill="var(--navy)"/>
      </svg>

      <h1 class="copy headline">RESIDENTIAL &amp;<br>COMMERCIAL<br>BUILDERS</h1>
      <p class="copy tagline">Quality Construction Services</p>
      <p class="copy call-to-action">NEED A BUILDER? CALL US TODAY!</p>
      <p class="copy phone">022 583 7092</p>
      <p class="copy website">www.harbourframeworks.co.nz</p>

      <div class="brand-plate">
        <span class="brand-square"></span>
        <span class="brand-name">Harbour<br>Frameworks</span>
      </div>
    </div>
  </div>
</div>
</body>
</html>
```